We need a business card design for a new company based in Queensland, Australia using our new logo (attached) using similar or complimentary colours and showing a softness and honesty. On the back we would like space to write three appointment or session times.ie. Session 1.... Session 2... Session 3.

Industry/Entity Type

Business

Contact Information for Business Card

name, title, mobile, email, web, address, facebook,

Requirements
Must have
• on back of card must have following:
• For information about Tranquivant Therapy please visit www.thevalendrawork.com
• Please use the registered symbol of an R in a circle at end of Tranquivant Therapy please.

```html
<!DOCTYPE html>
<html lang="en">
<head>
<meta charset="utf-8">
<title>Quiet Harbour Wellness – Business Card</title>
<link href="https://fonts.googleapis.com/css2?family=Questrial&family=Arimo:wght@400&display=swap" rel="stylesheet">
<style>
  :root {
    --bg: #e9e7e3;
    --card-white: #ffffff;
    --brand-blue: #1f74c4;
    --band-blue: #2a8fd6;
    --grad-light: #27b9dc;
    --grad-dark: #1f5fbf;
    --accent-green: #8cc63f;
    --ink: #1a1a1a;
    --icon-bg: #111111;
  }
  * { margin: 0; padding: 0; box-sizing: border-box; }
  html, body { width: 1200px; height: 858px; overflow: hidden; background: var(--bg); }
  .canvas { position: relative; width: 1200px; height: 858px; }

  .card {
    position: absolute;
    width: 560px; height: 320px;
    border-radius: 3px;
    box-shadow: 0 10px 26px rgba(0,0,0,.18);
    overflow: hidden;
  }

  /* Front */
  .card-front { left: 40px; top: 90px; background: var(--card-white); }
  .front-band {
    position: absolute; left: 0; right: 0; bottom: 0; height: 54px;
    background: var(--band-blue);
  }
  .brand-mark {
    position: absolute; left: 34px; bottom: 26px;
    width: 56px; height: 56px; border-radius: 50%;
    background: var(--accent-green);
    border: 5px solid var(--card-white);
  }
  .brand-lockup {
    position: absolute; left: 40px; top: 34px;
    font-family: "Questrial", sans-serif;
    color: var(--brand-blue);
  }
  .brand-name { font-size: 26px; letter-spacing: .5px; line-height: 1.1; }
  .brand-sub { font-size: 19px; line-height: 1.3; margin-left: 52px; color: var(--accent-green); }

  .divider {
    position: absolute; left: 250px; right: 0; top: 104px;
    height: 1.5px; background: var(--band-blue);
  }

  .contact-block {
    position: absolute; left: 250px; top: 112px;
    font-family: "Arimo", sans-serif; color: var(--ink);
  }
  .person-name { font-size: 22px; line-height: 1.1; }
  .person-title { font-size: 10.5px; line-height: 1.3; margin-top: 3px; }
  .contact-list { list-style: none; margin-top: 8px; }
  .contact-item {
    display: flex; align-items: center; gap: 8px;
    font-size: 13px; line-height: 1; height: 19px;
  }
  .icon {
    width: 15px; height: 15px; background: var(--icon-bg);
    display: flex; align-items: center; justify-content: center; flex: none;
  }

  /* Back */
  .card-back {
    left: 600px; top: 450px;
    background: linear-gradient(225deg, var(--grad-dark) 0%, var(--band-blue) 55%, var(--grad-light) 100%);
    display: flex; flex-direction: column; align-items: center; justify-content: center;
    padding: 26px 50px;
    font-family: "Questrial", sans-serif; color: #ffffff; text-align: center;
  }
  .back-mark {
    width: 34px; height: 34px; border-radius: 50%;
    background: #ffffff; margin: 0 auto 10px;
  }
  .card-back .brand-name { font-size: 24px; }
  .card-back .brand-sub { font-size: 18px; margin-left: 0; color: #ffffff; }
  .session-list { list-style: none; width: 100%; margin-top: 16px; }
  .session-line {
    display: flex; align-items: flex-end; gap: 8px;
    font-size: 14px; height: 26px; text-align: left;
  }
  .session-line::after {
    content: ""; flex: 1; border-bottom: 1px solid rgba(255,255,255,.75); margin-bottom: 4px;
  }
  .info-note { font-size: 11.5px; margin-top: 14px; opacity: .95; }
</style>
</head>
<body>
<main class="canvas">

  <section class="card card-front" aria-label="Card front">
    <div class="front-band"></div>
    <div class="brand-mark"></div>
    <div class="brand-lockup">
      <div class="brand-name">QUIET HARBOUR WELLNESS</div>
      <div class="brand-sub">with Tranquivant Therapy®</div>
    </div>
    <div class="divider"></div>
    <div class="contact-block">
      <div class="person-name">Maren Holloway</div>
      <div class="person-title">Tranquivant Therapy Foundational Practitioner<br>&amp; Valendra Certified Practitioner</div>
      <ul class="contact-list">
        <li class="contact-item">
          <span class="icon"><svg width="10" height="10" viewBox="0 0 24 24"><path fill="#8cc63f" d="M6.6 10.8a15 15 0 0 0 6.6 6.6l2.2-2.2c.3-.3.7-.4 1-.2 1.1.4 2.3.6 3.6.6.6 0 1 .4 1 1V20c0 .6-.4 1-1 1C10.6 21 3 13.4 3 4c0-.6.4-1 1-1h3.5c.6 0 1 .4 1 1 0 1.3.2 2.5.6 3.6.1.3 0 .7-.2 1z"/></svg></span>
          0400 136 528
        </li>
        <li class="contact-item">
          <span class="icon"><svg width="10" height="10" viewBox="0 0 24 24"><rect x="2" y="5" width="20" height="14" fill="#8cc63f"/><path d="M2 5l10 8 10-8" fill="none" stroke="#111" stroke-width="2"/></svg></span>
          maren@quietharbourwellness.com.au
        </li>
        <li class="contact-item">
          <span class="icon"><svg width="10" height="10" viewBox="0 0 24 24"><circle cx="12" cy="12" r="9" fill="none" stroke="#8cc63f" stroke-width="2.5"/><path d="M3 12h18M12 3c3 3 3 15 0 18M12 3c-3 3-3 15 0 18" fill="none" stroke="#8cc63f" stroke-width="2"/></svg></span>
          www.quietharbourwellness.com.au
        </li>
        <li class="contact-item">
          <span class="icon"><svg width="10" height="10" viewBox="0 0 24 24"><path fill="#8cc63f" d="M12 2a7 7 0 0 0-7 7c0 5 7 13 7 13s7-8 7-13a7 7 0 0 0-7-7zm0 9.5A2.5 2.5 0 1 1 12 6.5a2.5 2.5 0 0 1 0 5z"/></svg></span>
          14 Wattle Crest Rd, Coolum, Qld 4573
        </li>
      </ul>
    </div>
  </section>

  <section class="card card-back" aria-label="Card back">
    <div class="back-mark"></div>
    <div class="brand-name">QUIET HARBOUR WELLNESS</div>
    <div class="brand-sub">with Tranquivant Therapy®</div>
    <ul class="session-list">
      <li class="session-line">Session 1</li>
      <li class="session-line">Session 2</li>
      <li class="session-line">Session 3</li>
    </ul>
    <p class="info-note">For information about Tranquivant Therapy® please visit www.thevalendrawork.com</p>
  </section>

</main>
</body>
</html>
```